THE BRISK HOLLOW BEER

I want a beerlabel for this project.
It has to be enjoyable to look at. Some funny images and maybe some quotes on it.
This beer is about friends grabbing a pint in a pub.
Colors free to use except shiny colors I don't like.
The alcohol content is 5,7 % ABV 330ML
Target Market(s)
Young people 22 to 30 years old
Font styles to use
Serif
Decorative
Script
Colors
ffffff
000000
feeeee
Requirements
Must have
- coolness, some trendy design.
- Make sure it is a label and not a total bottle wrap.
Nice to have
- it has to feel good to drink.
Should not have
- shiny colors

```html
<!DOCTYPE html>
<html lang="en">
<head>
<meta charset="utf-8">
<title>The Brisk Hollow Beer – Label</title>
<link rel="stylesheet" href="https://fonts.googleapis.com/css2?family=Josefin+Sans:wght@700&family=Montserrat:wght@800&display=swap">
<style>
  :root {
    --ink: #000000;
    --paper: #ffffff;
    --blush: #fde6e6;
    --backdrop: #e4e4e4;
  }
  html, body {
    margin: 0;
    padding: 0;
    width: 1200px;
    height: 1198px;
    overflow: hidden;
    background: var(--backdrop);
  }
  .label {
    position: absolute;
    left: 218px;
    top: 59px;
    width: 765px;
    height: 1080px;
    background: var(--paper);
    overflow: hidden;
  }
  .label__cross {
    position: absolute;
    inset: 0;
  }
  .label__hop {
    position: absolute;
    left: 322px;
    top: 48px;
    width: 120px;
    height: 165px;
    background: var(--ink);
    border-radius: 50% 50% 45% 45% / 40% 40% 60% 60%;
  }
  .label__title {
    position: absolute;
    left: 0;
    right: 0;
    top: 272px;
    margin: 0;
    text-align: center;
    font-family: "Josefin Sans", sans-serif;
    font-weight: 700;
    font-size: 116px;
    line-height: 127px;
    letter-spacing: 4px;
    color: var(--ink);
  }
  .label__title span { display: block; }
  .label__info {
    position: absolute;
    left: 140px;
    width: 485px;
    top: 808px;
    font-family: "Montserrat", sans-serif;
    font-weight: 800;
    font-size: 23px;
    color: var(--ink);
  }
  .info-row {
    height: 56px;
    border-top: 3px solid var(--ink);
    display: flex;
    align-items: center;
    justify-content: center;
  }
  .info-row:last-child { border-bottom: 3px solid var(--ink); }
  .info-row--specs { justify-content: stretch; }
  .info-row--specs .spec {
    flex: 1;
    text-align: center;
  }
  .info-row--specs .spec + .spec {
    border-left: 3px solid var(--ink);
    height: 36px;
    line-height: 36px;
  }
  .info-row--specs .spec:first-child { line-height: 36px; }
</style>
</head>
<body>
  <div class="label">
    <svg class="label__cross" viewBox="0 0 765 1080" width="765" height="1080" aria-hidden="true">
      <polygon points="0,0 150,0 765,1080 615,1080" fill="var(--blush)"/>
      <polygon points="615,0 765,0 150,1080 0,1080" fill="var(--blush)"/>
    </svg>
    <div class="label__hop" role="img" aria-label="Black hop cone illustration"></div>
    <h1 class="label__title">
      <span>THE</span>
      <span>BRISK</span>
      <span>HOLLOW</span>
      <span>BEER</span>
    </h1>
    <div class="label__info">
      <div class="info-row">DEEP BALANCED AND FLAVORFUL</div>
      <div class="info-row">HAND CRAFTED IN ............................</div>
      <div class="info-row info-row--specs">
        <span class="spec">5,7 % ABV</span>
        <span class="spec">330 ML</span>
      </div>
    </div>
  </div>
</body>
</html>
```